Business Card for a Child Psychologist

I am a psychologist working with children and families and need a business card to give to clients and referral sources. I see children of all ages, so it should not look too young - as it will be for older children too. My work involves dealing with families in difficult situations, likes divorce, or with issues such as depression and anxiety. The design should communicate that I provide an open,warm, friendly, and caring atmosphere. I want to convey a sense of hope and positivity. Using colors like blues, purples

Target Market(s)

Families, doctors, family law attorneys

Industry/Entity Type

Psychology

Contact Information for Business Card

Dana Whitlow, Ph.D.
462 W. Marbury Row, Suite 2100
Chicago, Illinois 60688
312-555-0173
drdanajwhitlow@mailvista.example

Font styles to use
Script

Requirements
Must have
• A Logo to go with the details of my contact information.
Should not have
• Nothing in the shape of a brain. Nothing sad, or that looks too clinical.

```html
<!DOCTYPE html>
<html lang="en">
<head>
<meta charset="utf-8">
<title>Dana Whitlow, Ph.D. — Business Card</title>
<link href="https://fonts.googleapis.com/css2?family=Dancing+Script:wght@500;700&family=Titillium+Web:wght@400;600&family=Arimo:wght@700&display=swap" rel="stylesheet">
<style>
  :root {
    --page: #efefef;
    --card-white: #ffffff;
    --ink: #2a2a2a;
    --salmon: #fe9699;
    --pink: #f76d8d;
    --rose: #ef4a78;
    --navy: #2c3680;
    --teal: #23a594;
    --lavender: #a99bee;
    --back-navy: #16226f;
    --back-teal: #109b89;
    --back-purple: #621d78;
  }
  html, body {
    margin: 0;
    width: 1200px;
    height: 1200px;
    overflow: hidden;
    background: var(--page);
  }
  .sheet {
    position: relative;
    width: 1200px;
    height: 1200px;
  }
  .card {
    position: absolute;
    left: 230px;
    width: 740px;
    height: 453px;
    display: block;
    box-shadow: 0 6px 18px rgba(0,0,0,0.18);
  }
  .card--front { top: 100px; }
  .card--back { top: 646px; }
  .script { font-family: "Dancing Script", cursive; }
  .script--light { font-weight: 500; }
  .script--bold { font-weight: 700; }
  .title { font-family: "Titillium Web", sans-serif; font-weight: 600; }
  .contact { font-family: "Arimo", sans-serif; font-weight: 700; fill: var(--ink); }
</style>
</head>
<body>
<main class="sheet">

  <!-- Front: contact side -->
  <svg class="card card--front" viewBox="0 0 926 566" xmlns="http://www.w3.org/2000/svg" aria-label="Business card front">
    <defs>
      <linearGradient id="front-panel-tone" x1="0" y1="0" x2="0" y2="1">
        <stop offset="0" stop-color="var(--salmon)"/>
        <stop offset="0.2" stop-color="var(--rose)"/>
        <stop offset="0.36" stop-color="var(--navy)"/>
        <stop offset="0.64" stop-color="var(--navy)"/>
        <stop offset="0.8" stop-color="#7a5fc8"/>
        <stop offset="1" stop-color="var(--lavender)"/>
      </linearGradient>
    </defs>
    <rect class="card-face" width="926" height="566" fill="var(--card-white)" stroke="#9a9a9a" stroke-width="1.5"/>

    <polygon class="feature-panel" role="img" aria-label="Decorative colour panel in pink, navy and lavender tones"
      points="0,0 318,0 475,129 580,283 475,437 318,566 0,566" fill="url(#front-panel-tone)"/>

    <g class="name-block" fill="#ffffff">
      <text x="406" y="285" text-anchor="end" font-size="48" class="script"><tspan class="script--light">Dana </tspan><tspan class="script--bold">Whitlow,</tspan><tspan class="script--light"> Ph.D</tspan></text>
      <text x="406" y="318" text-anchor="end" font-size="27" class="title">Psychologist</text>
    </g>

    <g class="contact-list">
      <text x="826" y="308" text-anchor="end" font-size="19" class="contact">312-555-0173</text>
      <text x="826" y="389" text-anchor="end" font-size="17.5" class="contact">drdanajwhitlow@mailvista.example</text>
      <text x="826" y="455" text-anchor="end" font-size="18.5" class="contact">462 W. Marbury Row, Suite 2100</text>
      <text x="826" y="485" text-anchor="end" font-size="18.5" class="contact">Chicago, Illinois 60688</text>

      <g class="icon icon--phone" transform="translate(838,277)">
        <rect width="47" height="47" fill="var(--teal)"/>
        <path d="M14 12 l6 -2 l4 8 l-4 3 q3 6 8 9 l3 -4 l8 4 l-2 6 q-6 3 -14 -4 q-8 -7 -9 -20 z" fill="#ffffff"/>
      </g>
      <g class="icon icon--globe" transform="translate(838,359)">
        <rect width="47" height="47" fill="var(--rose)"/>
        <g fill="none" stroke="#ffffff" stroke-width="2.2">
          <circle cx="23.5" cy="23.5" r="14"/>
          <ellipse cx="23.5" cy="23.5" rx="6" ry="14"/>
          <line x1="9.5" y1="23.5" x2="37.5" y2="23.5"/>
          <line x1="11.5" y1="16" x2="35.5" y2="16"/>
          <line x1="11.5" y1="31" x2="35.5" y2="31"/>
        </g>
      </g>
      <g class="icon icon--pin" transform="translate(838,441)">
        <rect width="47" height="47" fill="var(--salmon)"/>
        <path d="M23.5 9 a10 10 0 0 1 10 10 c0 8 -10 19 -10 19 c0 0 -10 -11 -10 -19 a10 10 0 0 1 10 -10 z" fill="#ffffff"/>
        <circle cx="23.5" cy="19" r="4" fill="var(--salmon)"/>
      </g>
    </g>
  </svg>

  <!-- Back: name side -->
  <svg class="card card--back" viewBox="0 0 926 566" xmlns="http://www.w3.org/2000/svg" aria-label="Business card back">
    <defs>
      <linearGradient id="back-panel-tone" x1="0" y1="0" x2="1" y2="0">
        <stop offset="0" stop-color="var(--back-purple)"/>
        <stop offset="1" stop-color="var(--back-navy)"/>
      </linearGradient>
    </defs>
    <rect class="card-face" width="926" height="566" fill="var(--back-navy)"/>
    <rect class="feature-panel" role="img" aria-label="Decorative colour wash in purple and navy tones"
      x="0" y="0" width="620" height="566" fill="url(#back-panel-tone)"/>
    <g class="name-block">
      <text x="803" y="287" text-anchor="end" font-size="88" class="script"><tspan class="script--light" fill="#ffffff">Dana </tspan><tspan class="script--bold" fill="var(--back-teal)">Whitlow,</tspan><tspan class="script--light" fill="#ffffff"> Ph.D</tspan></text>
      <text x="798" y="344" text-anchor="end" font-size="50" class="title" fill="#ffffff">Psychologist</text>
    </g>
  </svg>

</main>
</body>
</html>
```